Wordpress Web Design Project for Upmarket Trendy Modern Travel Agency

We are a independent travel agency that does not offer online bookings (at this stage). We offer quality service and this needs to be reflected somehow in the design i.e. good old fashioned service.

Looking for wordpress Design for Travel Site

Company Name Voyage Harbor

www.voyageharborexample.com.au

Looking for something outside the box and not from layout goblin.

Something uniquely different !

Target Market(s)

Everyone

Industry/Entity Type

Travel

Requirements
Must have
• 1. Booking form
2. Seo friendly layout
3. Everything should be managed from wordpress admin

```html
<!DOCTYPE html>
<html lang="en">
<head>
<meta charset="utf-8">
<title>Voyage Harbor</title>
<link rel="stylesheet" href="https://fonts.googleapis.com/css2?family=Oswald:wght@500;600&family=Arimo:wght@400;700&display=swap">
<style>
:root{
  --navy:#0f2a42;
  --navy-dark:#051423;
  --nav-bg:#0c2236;
  --gold:#f6b800;
  --gold-dark:#e59a00;
  --panel:#4b7596;
  --panel-light:#5a83a3;
  --page:#d5e0ea;
  --text:#2b3a48;
  --muted:#7f96ab;
  --white:#ffffff;
  --heading:#13314d;
}
*{box-sizing:border-box;margin:0;padding:0}
html,body{width:1091px;height:1200px;overflow:hidden}
body{position:relative;background:var(--page);font-family:'Arimo',Arial,sans-serif;color:var(--text)}
.abs{position:absolute}
.header{left:0;top:0;width:1091px;height:66px;background:linear-gradient(#ffffff,#eef2f6)}
.brand{left:196px;top:18px;display:flex;align-items:center;gap:8px;font-family:'Arimo',Arial,sans-serif;font-weight:700;font-size:21px;color:var(--navy)}
.brand-dot{width:12px;height:12px;border-radius:50%;background:var(--gold)}
.search{left:744px;top:23px;width:150px;height:25px;border-radius:5px;background:#6488a6;display:flex;align-items:center}
.search span{flex:1;color:#eaf1f7;font-size:9px;text-align:center}
.search .btn{width:28px;height:25px;background:#4d7190;border-radius:0 5px 5px 0;display:flex;align-items:center;justify-content:center}
.nav{left:0;top:66px;width:1091px;height:51px;background:linear-gradient(#10273c,#071a2b)}
.nav ul{list-style:none;position:absolute;left:196px;top:0;width:698px;height:51px;display:flex;align-items:center;justify-content:space-between}
.nav li{font-family:'Oswald',sans-serif;font-weight:500;font-size:14px;color:var(--white);padding:0 10px;border-left:1px solid #2c4358;line-height:26px}
.nav li:first-child{border-left:none;color:var(--gold);padding-left:4px}
.hero{left:0;top:117px;width:1091px;height:382px;background:linear-gradient(180deg,#3d4f4a 0%,#4a9aa6 22%,#6fc6cc 45%,#9fdad8 70%,#e4ebe6 100%)}
.h2{font-family:'Oswald',sans-serif;font-weight:600;color:var(--heading);font-size:17px}
.numbers{left:196px;top:524px;width:174px}
.numbers h3{font-size:10.5px;font-weight:700;color:var(--heading);margin:12px 0 4px 2px;letter-spacing:.3px}
.numbers ul{list-style:none}
.numbers li{display:flex;align-items:center;gap:10px;height:22px;font-size:9px;color:#3f4f5e;border-bottom:1px dotted #7d8ea0}
.numbers li:last-child{border-bottom:none}
.tab{left:404px;top:520px;width:203px;height:34px;background:var(--panel);border-radius:5px 5px 0 0;color:#dbe8f3;font-family:'Oswald',sans-serif;font-weight:600;font-size:16px;padding:6px 0 0 45px}
.panel{left:404px;top:552px;width:490px;height:136px;background:var(--panel);border-radius:0 5px 5px 5px}
.lbl{font-size:9.5px;font-weight:700;color:var(--white)}
.field{height:20px;background:var(--white);border-radius:5px;font-size:8.5px;color:#444;display:flex;align-items:center}
.spin{justify-content:space-between;padding-left:8px;background:linear-gradient(90deg,#fff 70%,#2e4a62 70%)}
.spin i{width:16px;display:flex;justify-content:center}
.submit{left:806px;top:638px;width:69px;height:22px;border-radius:6px;background:linear-gradient(var(--gold),var(--gold-dark));font-family:'Oswald',sans-serif;font-weight:600;font-size:11px;color:#1b2430;display:flex;align-items:center;justify-content:center}
.touch{left:689px;top:524px;font-size:16px}
.social{left:784px;top:524px;display:flex;gap:7px}
.social span{width:22px;height:22px;border-radius:50%}
.welcome-img{left:404px;top:739px;width:181px;height:121px;background:linear-gradient(180deg,#1a6ec5 0%,#4a9ae0 55%,#8fd0dd 80%,#e8f0ea 100%)}
.welcome-text{left:598px;top:737px;width:296px;font-size:8.7px;line-height:14.6px;text-align:justify;color:#2d3b48}
.more{left:817px;top:835px;width:76px;height:22px;border-radius:6px;background:linear-gradient(var(--gold),var(--gold-dark));font-family:'Oswald',sans-serif;font-weight:600;font-size:11px;color:#1b2430;display:flex;align-items:center;justify-content:center}
.footer{left:0;top:941px;width:1091px;height:215px;background:var(--navy-dark)}
.footer-line{left:0;top:980px;width:1091px;border-top:1px dotted #2e4b66}
.fh{font-family:'Oswald',sans-serif;font-weight:600;color:var(--white);font-size:16px}
.date{left:196px;width:50px;height:48px;background:#4b6a85;color:var(--white);font-family:'Oswald',sans-serif;font-weight:600;text-align:center;line-height:1}
.date b{display:block;font-size:12px;padding-top:9px}
.date strong{display:block;font-size:19px}
.news{left:256px;width:151px;font-size:8.5px;line-height:14.5px;color:#6f8aa4;text-align:justify}
.news em{font-style:normal;font-weight:700;color:var(--gold)}
.news-sep{left:196px;top:1050px;width:210px;border-top:1px dotted #3a566f}
.view{left:332px;top:1110px;width:78px;height:26px;border-radius:6px;background:linear-gradient(var(--gold),var(--gold-dark));font-family:'Oswald',sans-serif;font-weight:600;font-size:11px;color:#1b2430;display:flex;align-items:center;justify-content:center}
.badge{left:469px;top:1000px;width:172px;height:99px;background:var(--white)}
.badge div{position:absolute;left:24px;top:18px;width:124px;height:48px;background:#1d2d3c}
.badge p{position:absolute;left:48px;top:74px;width:76px;height:12px;background:#21a8dc}
.arrow{top:1110px;width:26px;height:26px;border-radius:50%;display:flex;align-items:center;justify-content:center}
.contact{left:699px;top:997px;font-size:8.7px;line-height:17.5px;color:#7b96b0}
.contact b{color:var(--gold)}
.bottom{left:0;top:1156px;width:1091px;height:44px;background:#020b14}
.bottom ul{list-style:none;position:absolute;left:196px;top:16px;display:flex;font-size:8.7px;color:#d5dde5}
.bottom li{padding:0 8px;border-left:1px solid #d5dde5;line-height:10px}
.bottom li:first-child{padding-left:0;border-left:none;color:var(--gold)}
.copy{right:197px;top:16px;font-size:8.7px;color:#d5dde5}
</style>
</head>
<body>

<header class="abs header">
  <div class="abs brand"><span class="brand-dot"></span>Voyage Harbor</div>
  <div class="abs search"><span>Search..</span>
    <div class="btn"><svg width="14" height="14" viewBox="0 0 14 14"><circle cx="6" cy="6" r="4.2" fill="none" stroke="#e9f0f6" stroke-width="1.6"/><line x1="9" y1="9" x2="13" y2="13" stroke="#e9f0f6" stroke-width="2"/></svg></div>
  </div>
</header>

<nav class="abs nav">
  <ul>
    <li>Home</li><li>About us</li><li>Airfares</li><li>Hotels</li><li>Cars</li><li>Holidays</li><li>Cruises</li><li>Insurance</li><li>Contact Us</li>
  </ul>
</nav>

<div class="abs hero" role="img" aria-label="Photo of a wooden longtail boat on a turquoise lagoon below limestone cliffs"></div>

<section class="abs numbers">
  <h2 class="h2">World wide Numbers</h2>
  <h3>Australian Phone Number</h3>
  <ul>
    <li><svg width="9" height="11" viewBox="0 0 9 11"><path d="M4.5 0a4 4 0 0 0-4 4c0 3 4 7 4 7s4-4 4-7a4 4 0 0 0-4-4z" fill="#0d1a26"/><circle cx="4.5" cy="4" r="1.5" fill="#d5e0ea"/></svg>Sydney - &nbsp;(+612) 5550 1234</li>
    <li><svg width="9" height="11" viewBox="0 0 9 11"><path d="M4.5 0a4 4 0 0 0-4 4c0 3 4 7 4 7s4-4 4-7a4 4 0 0 0-4-4z" fill="#0d1a26"/><circle cx="4.5" cy="4" r="1.5" fill="#d5e0ea"/></svg>Adelaide - &nbsp;(+618) 5550 2847</li>
    <li><svg width="9" height="11" viewBox="0 0 9 11"><path d="M4.5 0a4 4 0 0 0-4 4c0 3 4 7 4 7s4-4 4-7a4 4 0 0 0-4-4z" fill="#0d1a26"/><circle cx="4.5" cy="4" r="1.5" fill="#d5e0ea"/></svg>Brisbane - &nbsp;(+617) 5550 3961</li>
    <li><svg width="9" height="11" viewBox="0 0 9 11"><path d="M4.5 0a4 4 0 0 0-4 4c0 3 4 7 4 7s4-4 4-7a4 4 0 0 0-4-4z" fill="#0d1a26"/><circle cx="4.5" cy="4" r="1.5" fill="#d5e0ea"/></svg>Canberra - &nbsp;(+612) 5550 4172</li>
    <li><svg width="9" height="11" viewBox="0 0 9 11"><path d="M4.5 0a4 4 0 0 0-4 4c0 3 4 7 4 7s4-4 4-7a4 4 0 0 0-4-4z" fill="#0d1a26"/><circle cx="4.5" cy="4" r="1.5" fill="#d5e0ea"/></svg>Melbourne - &nbsp;(+613) 5550 5683</li>
    <li><svg width="9" height="11" viewBox="0 0 9 11"><path d="M4.5 0a4 4 0 0 0-4 4c0 3 4 7 4 7s4-4 4-7a4 4 0 0 0-4-4z" fill="#0d1a26"/><circle cx="4.5" cy="4" r="1.5" fill="#d5e0ea"/></svg>Australia Wide FAX - (+612) 555</li>
  </ul>
  <h3 style="margin-top:14px">International Phone Number</h3>
  <ul>
    <li><svg width="9" height="11" viewBox="0 0 9 11"><path d="M4.5 0a4 4 0 0 0-4 4c0 3 4 7 4 7s4-4 4-7a4 4 0 0 0-4-4z" fill="#0d1a26"/><circle cx="4.5" cy="4" r="1.5" fill="#d5e0ea"/></svg>&nbsp; Thailand - &nbsp;(+66) 38 555 017</li>
    <li><svg width="9" height="11" viewBox="0 0 9 11"><path d="M4.5 0a4 4 0 0 0-4 4c0 3 4 7 4 7s4-4 4-7a4 4 0 0 0-4-4z" fill="#0d1a26"/><circle cx="4.5" cy="4" r="1.5" fill="#d5e0ea"/></svg>&nbsp; Thailand FAX - (+66) 38 555 092</li>
    <li><svg width="9" height="11" viewBox="0 0 9 11"><path d="M4.5 0a4 4 0 0 0-4 4c0 3 4 7 4 7s4-4 4-7a4 4 0 0 0-4-4z" fill="#0d1a26"/><circle cx="4.5" cy="4" r="1.5" fill="#d5e0ea"/></svg>&nbsp; Bangkok - &nbsp;(+66) 2 5550183</li>
    <li><svg width="9" height="11" viewBox="0 0 9 11"><path d="M4.5 0a4 4 0 0 0-4 4c0 3 4 7 4 7s4-4 4-7a4 4 0 0 0-4-4z" fill="#0d1a26"/><circle cx="4.5" cy="4" r="1.5" fill="#d5e0ea"/></svg>&nbsp; Hong Kong - &nbsp;(+852) 5550 2716</li>
    <li><svg width="9" height="11" viewBox="0 0 9 11"><path d="M4.5 0a4 4 0 0 0-4 4c0 3 4 7 4 7s4-4 4-7a4 4 0 0 0-4-4z" fill="#0d1a26"/><circle cx="4.5" cy="4" r="1.5" fill="#d5e0ea"/></svg>&nbsp; USA - &nbsp;(+1) 213 555 0147</li>
    <li><svg width="9" height="11" viewBox="0 0 9 11"><path d="M4.5 0a4 4 0 0 0-4 4c0 3 4 7 4 7s4-4 4-7a4 4 0 0 0-4-4z" fill="#0d1a26"/><circle cx="4.5" cy="4" r="1.5" fill="#d5e0ea"/></svg>&nbsp; UK - &nbsp;(+44) 208 555 0193</li>
  </ul>
</section>

<div class="abs tab">Quick Search</div>
<div class="abs h2 touch">Get in Touch :</div>
<div class="abs social" role="img" aria-label="Social network links">
  <span style="background:#f08a24"></span><span style="background:#e8642a"></span><span style="background:#6fb7e8"></span><span style="background:#3a5c9a"></span>
</div>
<form class="abs panel" aria-label="Quick search booking form"></form>

<span class="abs lbl" style="left:421px;top:572px">Leaving from</span>
<span class="abs lbl" style="left:561px;top:572px">Going to</span>
<span class="abs lbl" style="left:693px;top:572px">Adults</span>
<span class="abs lbl" style="left:757px;top:572px">Seniors</span>
<span class="abs lbl" style="left:821px;top:572px">Chield</span>
<div class="abs field" style="left:421px;top:587px;width:126px"></div>
<div class="abs field spin" style="left:557px;top:587px;width:126px;background:linear-gradient(90deg,#fff 84%,#2e4a62 84%)">Kerala/ moonnar<i><svg width="8" height="6" viewBox="0 0 8 6"><path d="M1 1l3 3 3-3" fill="none" stroke="#fff" stroke-width="1.6"/></svg></i></div>
<div class="abs field spin" style="left:693px;top:587px;width:54px">19-64<i><svg width="8" height="14" viewBox="0 0 8 14"><path d="M1 5l3-3 3 3M1 9l3 3 3-3" fill="none" stroke="#fff" stroke-width="1.4"/></svg></i></div>
<div class="abs field spin" style="left:757px;top:587px;width:54px">&nbsp;65+<i><svg width="8" height="14" viewBox="0 0 8 14"><path d="M1 5l3-3 3 3M1 9l3 3 3-3" fill="none" stroke="#fff" stroke-width="1.4"/></svg></i></div>
<div class="abs field spin" style="left:821px;top:587px;width:54px">0-18<i><svg width="8" height="14" viewBox="0 0 8 14"><path d="M1 5l3-3 3 3M1 9l3 3 3-3" fill="none" stroke="#fff" stroke-width="1.4"/></svg></i></div>

<span class="abs lbl" style="left:421px;top:624px">Budject</span>
<span class="abs lbl" style="left:531px;top:624px">Departing</span>
<span class="abs lbl" style="left:596px;top:624px">Time</span>
<span class="abs lbl" style="left:667px;top:624px">Returning</span>
<span class="abs lbl" style="left:733px;top:624px">Time</span>
<div class="abs field" style="left:421px;top:639px;width:100px"></div>
<div class="abs field" style="left:531px;top:639px;width:56px"></div>
<div class="abs field spin" style="left:596px;top:639px;width:61px;padding-left:20px">Any<i><svg width="8" height="14" viewBox="0 0 8 14"><path d="M1 5l3-3 3 3M1 9l3 3 3-3" fill="none" stroke="#fff" stroke-width="1.4"/></svg></i></div>
<div class="abs field" style="left:667px;top:639px;width:56px"></div>
<div class="abs field spin" style="left:733px;top:639px;width:61px;padding-left:20px">Any<i><svg width="8" height="14" viewBox="0 0 8 14"><path d="M1 5l3-3 3 3M1 9l3 3 3-3" fill="none" stroke="#fff" stroke-width="1.4"/></svg></i></div>
<div class="abs submit">Submit</div>

<h2 class="abs h2" style="left:405px;top:705px">Welcome to Voyage Harbor</h2>
<div class="abs welcome-img" role="img" aria-label="Photo of a hammock under a palm tree on a tropical beach"></div>
<p class="abs welcome-text">Lorem Ipsum is simply dummy text of the printing and typesetting industry. Lorem Ipsum has been the industry's standard dummy text ever since the 1500s, It has survived not only five centuries when an unknown printer took a galley of type and scrambled it to make a type specimen book. It has survived not only five centuries, but also the leap into electronic typesetting, remaining essentially unchanged.</p>
<div class="abs more">Ream More</div>

<footer class="abs footer"></footer>
<div class="abs footer-line"></div>
<h2 class="abs fh" style="left:197px;top:951px">Latest News</h2>
<h2 class="abs fh" style="left:506px;top:949px">Members Of</h2>
<h2 class="abs fh" style="left:699px;top:949px">Quick Contact</h2>

<div class="abs date" style="top:997px"><b>NOV</b><strong>5</strong></div>
<p class="abs news" style="top:997px">Lorem Ipsum is simply dummy text of the printing and typesetting industry. Lorem Ipsum <em>has been the industry's</em></p>
<div class="abs news-sep"></div>
<div class="abs date" style="top:1055px"><b>NOV</b><strong>7</strong></div>
<p class="abs news" style="top:1056px"><em>Lorem Ipsum</em> is simply dummy text of the printing and typesetting industry. Lorem Ipsum has been the industry's</p>
<div class="abs view">View More</div>

<div class="abs badge" role="img" aria-label="Travel association member badge"><div></div><p></p></div>
<div class="abs arrow" style="left:524px;background:#000"><svg width="10" height="12" viewBox="0 0 10 12"><path d="M7 1L2 6l5 5" fill="none" stroke="#fff" stroke-width="2.4"/></svg></div>
<div class="abs arrow" style="left:559px;background:var(--gold)"><svg width="10" height="12" viewBox="0 0 10 12"><path d="M3 1l5 5-5 5" fill="none" stroke="#fff" stroke-width="2.4"/></svg></div>

<address class="abs contact" style="font-style:normal">
  <b>Address:</b> P.O Box 512 Marlow Bay NSW 2290<br>
  <b>Phone:</b> &nbsp;(+612) 5550 1234<br>
  <b>Call:</b> &nbsp;(+612) 5550 1234<br>
  <b>Fax:</b> (+612) 555 019 42<br>
  <b>E-mail:</b> sales@voyageharborexample.com.au<br>
  <b>web:</b> www.voyageharborexample.com.au
</address>

<div class="abs bottom">
  <ul><li>Home</li><li>About us</li><li>Airfares</li><li>Hotels</li><li>Cars</li><li>Holidays</li><li>Cruises</li><li>Insurance</li><li>Contact Us</li></ul>
</div>
<div class="abs copy">2012@All Rights Reserved.</div>

</body>
</html>
```